BrightpathHR Brochure

We need a Brochure design for a Human Resources company based in Windhoek Namibia. We do general HR admin, payroll, disciplinary hearings, recruitment. We would like a design which can be used to print hardcopies as well as pdf versions.

Industry/Entity Type

Human Resource

Colors

Designer to choose colors to be used in the design.

Requirements
Nice to have
• relevant pictures

```html
<!DOCTYPE html>
<html lang="en">
<head>
<meta charset="utf-8">
<title>BrightpathHR Brochure</title>
<link rel="stylesheet" href="https://fonts.googleapis.com/css2?family=Arimo:wght@700&family=Open+Sans:wght@400&display=swap">
<style>
  :root {
    --orange: #e8603a;
    --heading-orange: #e55a33;
    --gold: #fbb443;
    --white: #ffffff;
    --ink: #2b2b2b;
  }
  html, body {
    margin: 0;
    padding: 0;
    overflow: hidden;
    background: var(--white);
  }
  .brochure {
    position: relative;
    width: 1200px;
    height: 927px;
    overflow: hidden;
    background: var(--white);
  }
  .tile {
    position: absolute;
    box-sizing: border-box;
  }
  .photo-handshake-desk {
    left: 0; top: 0; width: 402px; height: 480px;
    background: linear-gradient(135deg, #4a3a2c 0%, #5d4835 35%, #2f3440 65%, #3e3126 100%);
  }
  .panel-approach {
    left: 402px; top: 0; width: 396px; height: 480px;
    background: var(--white);
  }
  .photo-handshake-office {
    left: 798px; top: 0; width: 402px; height: 480px;
    background: linear-gradient(160deg, #d9d6d1 0%, #b9b3ab 35%, #5a4c44 60%, #c7c3bd 100%);
  }
  .panel-welcome {
    left: 0; top: 480px; width: 400px; height: 447px;
    background: var(--orange);
  }
  .photo-calendar-planning {
    left: 400px; top: 480px; width: 398px; height: 447px;
    background: linear-gradient(150deg, #4b3a2e 0%, #e9e4da 35%, #f1ede6 60%, #5a4636 100%);
  }
  .panel-mission {
    left: 798px; top: 480px; width: 402px; height: 447px;
    background: var(--orange);
  }
  .heading {
    position: absolute;
    margin: 0;
    font-family: "Arimo", Arial, sans-serif;
    font-weight: 700;
    font-size: 43px;
    line-height: 1.18;
    letter-spacing: 0.01em;
  }
  .body-copy {
    position: absolute;
    margin: 0;
    font-family: "Open Sans", Arial, sans-serif;
    font-weight: 400;
    font-size: 16.5px;
    line-height: 22.6px;
    letter-spacing: 0.07em;
  }
  .panel-approach .heading { left: 30px; top: 128px; color: var(--heading-orange); }
  .panel-approach .body-copy { left: 25px; top: 259px; width: 345px; color: var(--ink); }
  .panel-welcome .heading { left: 32px; top: 572px; color: var(--gold); position: absolute; }
  .panel-welcome .heading, .panel-mission .heading { top: 92px; }
  .panel-welcome .heading { left: 32px; }
  .panel-welcome .body-copy { left: 35px; top: 169px; width: 340px; color: var(--white); }
  .panel-mission .heading { left: 40px; color: var(--gold); }
  .panel-mission .body-copy { left: 43px; top: 167px; width: 330px; color: var(--white); }
</style>
</head>
<body>
<main class="brochure">
  <div class="tile photo-handshake-desk" role="img" aria-label="Overhead photo of two business people shaking hands across a wooden desk with papers and a laptop"></div>

  <section class="tile panel-approach">
    <h2 class="heading">OUR<br>APPROACH</h2>
    <p class="body-copy">Each company is unique. One-size-fits-all approaches will never help your business reach its full potential. We deliver custom solutions, tailored to you – your industry, your culture, your one-of-a-kind challenges.</p>
  </section>

  <div class="tile photo-handshake-office" role="img" aria-label="Photo of a business handshake above an office desk with a laptop and documents"></div>

  <section class="tile panel-welcome">
    <h2 class="heading">WELCOME</h2>
    <p class="body-copy">We offer a range of HR consulting services, all designed to help your company reach its potential. Whether you're looking for a small tweak or complete overhaul, we have you covered. Our services are available a la carte so you can get precisely what you need.</p>
  </section>

  <div class="tile photo-calendar-planning" role="img" aria-label="Overhead photo of hands planning on a paper calendar and an open diary"></div>

  <section class="tile panel-mission">
    <h2 class="heading">MISSION</h2>
    <p class="body-copy">The mission of BrightpathHR is dedication to the highest quality of Customer Service, delivered with a sense of warmth and friendliness</p>
  </section>
</main>
</body>
</html>
```